" Um café onde o croissant é o produto carro chefe. Um local para um lanche rápido, com arquitetura premium e minimalista. Croissants especiais, produto premium, com receita francesa, e recheios salgados e doces. Além disso, temos cafés especiais para acompanhar os croissants. Um momento de indulgência no meio de um dia corrido. "

```html
<!DOCTYPE html>
<html lang="pt-BR">
<head>
<meta charset="utf-8">
<title>Mille&amp;Beurre — Cartão Fidelidade</title>
<link rel="stylesheet" href="https://fonts.googleapis.com/css2?family=Montserrat:ital,wght@0,200;0,700;0,800;1,800&family=Tinos&display=swap">
<style>
  :root {
    --canvas: #ecebe8;
    --ink: #0d0d0d;
    --paper: #ffffff;
    --gold-dark: #9a7a3a;
    --gold-light: #e6cf8e;
    --line-grey: #3a3a3a;
    --text-dark: #1a1a1a;
  }
  * { box-sizing: border-box; margin: 0; padding: 0; }
  html, body { width: 1200px; height: 1200px; overflow: hidden; }
  body { background: var(--canvas); position: relative; font-family: "Montserrat", sans-serif; }

  .card {
    position: absolute;
    left: 170px;
    width: 860px;
    height: 478px;
    border-radius: 70px 0 70px 0;
    overflow: hidden;
  }
  .card--front { top: 92px; background: var(--ink); }
  .card--back  { top: 630px; background: var(--paper); box-shadow: 0 0 0 1px #d8d8d8; }

  .brand-name {
    position: absolute;
    font-family: "Montserrat", sans-serif;
    font-weight: 200;
    letter-spacing: 2px;
    white-space: nowrap;
  }
  .card--front .brand-name {
    left: 0; width: 760px; top: 150px;
    text-align: center;
    font-size: 68px;
    color: var(--paper);
  }
  .card--back .brand-name {
    left: 48px; top: 66px;
    font-size: 50px;
    color: var(--text-dark);
  }

  .loyalty-title {
    position: absolute;
    right: 52px; top: 326px;
    text-align: right;
    color: var(--paper);
    line-height: 1;
  }
  .loyalty-title__kicker { display: block; font-weight: 700; font-size: 20px; letter-spacing: 1px; }
  .loyalty-title__main { display: block; font-weight: 800; font-style: italic; font-size: 30px; margin-top: 6px; }

  .gold-band {
    position: absolute; left: 0; right: 0;
    background: linear-gradient(90deg, var(--gold-dark), var(--gold-light) 35%, var(--gold-dark) 65%, var(--gold-light));
  }
  .white-rule { position: absolute; left: 0; right: 0; height: 3px; background: var(--paper); }
  .card--front .white-rule { top: 412px; }
  .card--front .gold-band { top: 422px; height: 14px; }

  .contact-block {
    position: absolute;
    left: 470px; top: 72px; width: 330px;
    font-family: "Tinos", serif;
    color: var(--text-dark);
    text-align: center;
  }
  .contact-block__phone {
    font-size: 19px;
    padding-bottom: 8px;
    border-bottom: 2px solid var(--line-grey);
  }
  .contact-block__line { font-size: 18px; margin-top: 16px; }
  .contact-block__line + .contact-block__line { margin-top: 6px; }

  .card--back .gold-band { top: 286px; height: 6px; }
  .stamp-area { position: absolute; left: 0; right: 0; top: 292px; bottom: 0; background: var(--ink); }
  .stamp-grid {
    position: absolute;
    left: 150px; top: 40px;
    display: grid;
    grid-template-columns: repeat(4, 86px);
    grid-template-rows: repeat(2, 58px);
    column-gap: 62px;
    row-gap: 22px;
  }
  .stamp { background: var(--paper); border-radius: 18px; }
</style>
</head>
<body>

  <section class="card card--front" aria-label="Frente do cartão fidelidade">
    <div class="brand-name">Mille&amp;Beurre</div>
    <div class="loyalty-title">
      <span class="loyalty-title__kicker">CARTÃO</span>
      <span class="loyalty-title__main">Fidelidade</span>
    </div>
    <div class="white-rule"></div>
    <div class="gold-band"></div>
  </section>

  <section class="card card--back" aria-label="Verso do cartão fidelidade">
    <div class="brand-name">Mille&amp;Beurre</div>
    <div class="contact-block">
      <p class="contact-block__phone">Telefone : (555) 010-4821</p>
      <p class="contact-block__line">Email: contato@millebeurre.com</p>
      <p class="contact-block__line">Web: millebeurre.com</p>
    </div>
    <div class="gold-band"></div>
    <div class="stamp-area">
      <div class="stamp-grid">
        <span class="stamp"></span><span class="stamp"></span><span class="stamp"></span><span class="stamp"></span>
        <span class="stamp"></span><span class="stamp"></span><span class="stamp"></span><span class="stamp"></span>
      </div>
    </div>
  </section>

</body>
</html>
```